Redesign of our homepage

We are a company that operates in the Wellness tourism sector. We are starting a project to redesign our homepage. See the screenshots. The main idea is that the banner image and the text on the banner are dynamically replaced depending on whether a user clicks on the "Thumb up" or the "Thumb down" icon.
You can see a live version of our homepage at http://demo.verdalumo.com

Industry/Entity Type

Health And Wellness

Coding

Coded - Design and coding required

Number of Pages Required

1 page

Requirements
Must have
• Must abide by style and look & feel of the current site.
It is important to demonstrate the functionality that enables the banner image and text being refreshed at each click of a ThumbUp or ThumbDown icons. In others words the Javascript must work.

Let me add some more context on the project.

Actually the thumb up and thumb down are possible answers to question/comment dynamically displayed at the location of the current text "Experience That Make You tell an unforgettable story".
An example of a comment/question is "I need a program that would help limit my stress levels and make me look great and feel fantastic". Or "I need an activity that will reduce my stress."
So a user would have to click on a thumb up or thumb down to approve or disapprove these questions/comments..
Based on this information, I think you could move the thumbs up to the left and right side of the text (the comment/question) respectively. And move the reset underneath in the middle.

Maybe it's a good idea to reduce the font size of that text as well.

And now to the dropdown list. We need only 2 of them, and not 3 as you have displayed.
One of them contain the list:
-- I need a weekend retreat
-- ! need a week or more retreat
The other would contain a list of countries.
The drop down values must be selected before the thumbs up and down thumbs are active.
Therefore you should move them above the question/comment text.
And finally about the thumbs and reset icons. Please put them in a round orange color and make them a bit bigger.

```html
<!DOCTYPE html>
<html lang="en">
<head>
<meta charset="utf-8">
<title>Verdalumo – Wellness Retreats</title>
<link rel="stylesheet" href="https://fonts.googleapis.com/css2?family=Nunito:wght@300;400;600;700;800&family=Pathway+Gothic+One&display=swap">
<style>
:root{
  --orange:#f7901e;
  --orange-dark:#e67e0a;
  --ink:#1f1f1f;
  --grey:#5a5a5a;
  --muted:#9a9a9a;
  --teal:#2bb4a6;
  --page:#f4fafc;
  --green-tick:#23a33a;
  --red-cross:#e3131b;
  --footer:#000;
  --pie-orange:#f29a37;
  --pie-green:#8fe0c5;
  --pie-green-dark:#64bfa2;
  --pie-blue:#1b5fa8;
}
*{box-sizing:border-box;margin:0;padding:0}
html,body{width:1200px;height:3233px;overflow:hidden}
body{position:relative;background:var(--page);font-family:'Nunito',sans-serif;color:var(--ink)}
.abs{position:absolute}

/* header */
.site-header{position:absolute;left:0;top:0;width:1200px;height:107px;background:#fff;z-index:5}
.brand{position:absolute;left:88px;top:30px;display:flex;align-items:center;gap:10px;font-weight:300;font-size:38px;color:var(--orange);letter-spacing:.5px}
.brand-dot{width:14px;height:14px;border-radius:50%;background:var(--orange)}
.main-nav{position:absolute;top:44px;font-size:14px;font-weight:600;color:#222;display:flex;align-items:center;gap:6px}
.btn-head{position:absolute;top:34px;height:35px;background:var(--orange);color:#fff;font-weight:700;font-size:16px;display:flex;align-items:center;justify-content:center;gap:7px}

/* category menu */
.cat-menu{position:absolute;left:404px;top:80px;width:753px;height:143px;background:rgba(255,255,255,.95);z-index:6}
.cat{position:absolute;width:134px;height:59px;color:#fff;font-size:13px;font-weight:600;display:flex;align-items:center;justify-content:center;text-shadow:0 1px 2px rgba(0,0,0,.5)}

/* hero */
.hero{position:absolute;left:0;top:107px;width:1200px;height:280px;background:linear-gradient(180deg,#7fb8e0 0%,#b9dcef 40%,#4fc3d3 75%,#14a9c4 100%)}
.hero-side{position:absolute;top:70px;height:150px;background:linear-gradient(180deg,#a2875f,#5f4a31)}
.prompt-panel{position:absolute;left:197px;top:144px;width:804px;height:262px;background:rgba(255,255,255,.6);border-radius:6px;z-index:3}
.prompt-select{position:absolute;top:88px;width:226px;height:32px;background:#fff;border:1px solid #ccc;font-size:14px;font-weight:700;padding:6px 12px;color:#222}
.prompt-select svg{position:absolute;right:10px;top:12px}
.prompt-text{position:absolute;left:120px;top:138px;width:564px;text-align:center;font-size:19px;font-weight:800;line-height:24px;color:#111}
.round-btn{position:absolute;border-radius:50%;background:var(--orange);display:flex;align-items:center;justify-content:center;box-shadow:0 2px 6px rgba(0,0,0,.2)}
.thumb{top:130px;width:64px;height:64px}
.reset{left:374px;top:196px;width:56px;height:56px}

/* sort */
.sort{position:absolute;left:323px;top:492px;font-size:18px;font-weight:600;color:#333;display:flex;align-items:center;gap:10px}
.sort-select{position:absolute;left:438px;top:484px;width:225px;height:44px;background:#fff;border:2px solid var(--orange);font-size:18px;color:#555;padding:9px 14px}

/* cards */
.card{position:absolute;left:0;width:1200px;height:560px}
.price-box{position:absolute;left:89px;top:0;width:207px;height:295px;background:#fff;border:2px solid var(--orange);padding:26px 0 0 19px}
.price-label{color:var(--orange);font-size:18px;margin-bottom:15px}
.spec{display:flex;align-items:center;gap:10px;font-size:15.5px;font-weight:600;height:29px;color:#222}
.spec svg{flex:none}
.eco{display:flex;align-items:center;gap:8px;font-size:16.5px;font-weight:600;height:40px}
.eco.first{margin-top:10px}
.card-photo{position:absolute;left:323px;top:0;width:522px;height:294px;border-radius:0 0 60px 0}
.fav{position:absolute;left:347px;top:25px;width:46px;height:46px;border-radius:50%;background:var(--orange);display:flex;align-items:center;justify-content:center}
.benefits{position:absolute;left:873px;top:0;width:236px;height:295px;background:var(--orange);border-radius:50px;color:#fff;text-align:center}
.benefits h3{font-family:'Pathway Gothic One',sans-serif;font-weight:400;font-size:32px;line-height:36px;margin-top:92px}
.read-more{position:absolute;left:0;right:0;top:236px;font-size:16px;font-weight:700;display:flex;justify-content:center;align-items:center;gap:10px}
.trip-info{position:absolute;left:323px;top:322px;width:400px}
.trip-title{font-family:'Pathway Gothic One',sans-serif;font-weight:400;font-size:32px;line-height:39px;letter-spacing:-.3px;color:#111}
.trip-from{font-size:21px;margin-top:12px;color:#222}
.trip-price{font-size:23px;font-weight:800;margin-top:4px}
.divider{position:absolute;left:748px;top:323px;width:1px;background:#ddd}
.features{position:absolute;left:788px;top:327px}
.feature{display:flex;align-items:center;gap:8px;font-size:17.5px;font-weight:600;color:#444;height:37px}
.btn-details{position:absolute;left:789px;top:477px;width:142px;height:44px;background:var(--orange);color:#fff;font-weight:800;font-size:15px;display:flex;align-items:center;justify-content:center}

/* pagination */
.pager{position:absolute;top:2318px;height:28px;border:1px solid #e3e3e3;background:#fff;font-size:12px;font-weight:600;display:flex;align-items:center;justify-content:center;color:#333}
.pager.active{background:var(--orange);border-color:var(--orange);color:#fff}
.pager.off{color:#c5c5c5}

/* charts */
.chart-title{position:absolute;width:500px;text-align:center;font-size:11px;color:#333}
.chart-sub{position:absolute;width:500px;text-align:center;font-size:9px;color:#444}
.legend{position:absolute;height:37px;border:1px solid #999;background:#fff;font-size:8px;color:#555;padding:4px 8px;line-height:14px}
.lg{display:inline-flex;align-items:center;gap:4px;margin-right:30px}
.lg i{display:inline-block;width:7px;height:7px;border-radius:50%}

/* footer */
.site-footer{position:absolute;left:0;top:2780px;width:1200px;height:453px}
.foot-col{position:absolute;top:115px;font-size:11.5px;color:#fff;font-weight:600;line-height:20px}
.foot-col h4{font-size:10px;color:var(--teal);font-weight:600;margin-bottom:8px;padding-bottom:14px;position:relative}
.foot-col h4::after{content:"";position:absolute;left:0;bottom:0;width:54px;height:1px;background:var(--teal)}
.foot-row{display:flex;align-items:center;gap:8px}
.copy{position:absolute;left:107px;top:372px;color:#fff;font-size:12px;font-weight:600}
.connect{position:absolute;left:835px;top:360px;color:#fff;font-size:12px;font-weight:600;display:flex;align-items:center;gap:6px}
.social{width:36px;height:36px;border-radius:50%;background:#2f8fd8;border:2px solid #fff}
.social.dark{background:#000}
</style>
</head>
<body>

<header class="site-header">
  <div class="brand"><span class="brand-dot"></span>verdalumo</div>
  <nav>
    <div class="main-nav" style="left:348px">EUR
      <svg width="12" height="8" viewBox="0 0 12 8"><path d="M1 1l5 5 5-5" stroke="#222" stroke-width="2" fill="none"/></svg></div>
    <div class="main-nav" style="left:414px">
      <svg width="20" height="14" viewBox="0 0 20 14"><path d="M10 2c2 3 2 6 0 10c-2-4-2-7 0-10zM2 6c4 0 7 3 8 7c-4 0-7-2-8-7zM18 6c-4 0-7 3-8 7c4 0 7-2 8-7z" fill="#222"/></svg>Wellness Retreats</div>
    <div class="main-nav" style="left:580px">
      <svg width="20" height="14" viewBox="0 0 20 14"><path d="M5 13a4 4 0 010-8a6 6 0 0111 1a3.5 3.5 0 010 7z" fill="#222"/></svg>Our Climate Pledge</div>
    <div class="main-nav" style="left:758px">
      <svg width="20" height="14" viewBox="0 0 20 14"><path d="M2 7l5-4 4 2 4-2 4 4-7 5z" fill="none" stroke="#222" stroke-width="1.6"/></svg>Partners</div>
  </nav>
  <div class="btn-head" style="left:865px;width:111px">
    <svg width="18" height="16" viewBox="0 0 18 16"><path d="M1 8h9M7 4l4 4-4 4M12 1h4v14h-4" stroke="#fff" stroke-width="2" fill="none"/></svg>Sign in</div>
  <div class="btn-head" style="left:995px;width:114px">
    <svg width="20" height="16" viewBox="0 0 20 16"><circle cx="7" cy="4.5" r="3.5" fill="#fff"/><path d="M0 15c0-5 14-5 14 0z" fill="#fff"/><path d="M16 4v6M13 7h6" stroke="#fff" stroke-width="2"/></svg>Sign up</div>
</header>

<div class="cat-menu">
  <div class="cat" role="img" aria-label="Ayurveda photo" style="left:10px;top:5px;background:linear-gradient(135deg,#8c3b91,#e07bb6)">Ayurveda</div>
  <div class="cat" role="img" aria-label="Yoga photo" style="left:158px;top:5px;background:linear-gradient(180deg,#2b5d8c,#0f2f4e)">Yoga</div>
  <div class="cat" role="img" aria-label="Detox photo" style="left:306px;top:5px;background:linear-gradient(135deg,#c9c3b3,#6b6556)">Detox</div>
  <div class="cat" role="img" aria-label="Fasting photo" style="left:453px;top:5px;background:linear-gradient(135deg,#e9c2ad,#b98b72)">Fasting</div>
  <div class="cat" role="img" aria-label="Anti-aging photo" style="left:601px;top:5px;background:linear-gradient(135deg,#3c3c3c,#d8d2cc)">Anti-Aging</div>
  <div class="cat" role="img" aria-label="Spa photo" style="left:10px;top:77px;background:linear-gradient(135deg,#7e5e4c,#d3b39c)">Spa</div>
  <div class="cat" role="img" aria-label="Pilates photo" style="left:158px;top:77px;background:linear-gradient(135deg,#d8d5cf,#8d8a84)">Pilate</div>
  <div class="cat" role="img" aria-label="Weight loss photo" style="left:306px;top:77px;background:linear-gradient(135deg,#5a0d12,#1f0b0b)">Weight Loss</div>
  <div class="cat" role="img" aria-label="Fitness photo" style="left:453px;top:77px;background:linear-gradient(135deg,#1a2436,#3b4d68)">Fitness</div>
  <div class="cat" role="img" aria-label="Thalassotherapy photo" style="left:601px;top:77px;background:linear-gradient(135deg,#8a7fb8,#c7bfe2)">Thalassotherapy</div>
</div>

<section class="hero" role="img" aria-label="Overwater bungalows on a tropical lagoon">
  <div class="hero-side" style="left:0;width:220px;border-radius:0 40px 0 0"></div>
  <div class="hero-side" style="left:1000px;width:200px;background:linear-gradient(180deg,#3f7d3a,#d8c9a4)"></div>
</section>
<svg width="1200" height="90" viewBox="0 0 1200 90" style="position:absolute;left:0;top:300px">
  <path d="M0 35C150 20 260 20 380 45S620 85 800 60S1050 20 1200 30V90H0z" fill="var(--page)"/>
</svg>

<div class="prompt-panel">
  <div class="prompt-select" style="left:164px">I need a weekend retreat
    <svg width="12" height="7" viewBox="0 0 12 7"><path d="M0 0h12L6 7z" fill="#888"/></svg></div>
  <div class="prompt-select" style="left:414px">Select a country
    <svg width="12" height="7" viewBox="0 0 12 7"><path d="M0 0h12L6 7z" fill="#888"/></svg></div>
  <div class="round-btn thumb" style="left:36px" aria-label="Thumb down">
    <svg width="34" height="34" viewBox="0 0 42 42"><path d="M6 6h9v18H6zM15 8c6-3 14-3 18 0c3 1 3 4 1 5c2 1 2 4 0 5c2 1 1 4-1 5h-9l2 8c0 3-3 4-4 2l-7-11z" fill="#fff"/></svg>
  </div>
  <p class="prompt-text">I need a program that would help limit my stress levels and make me look great and feel fantastic</p>
  <div class="round-btn thumb" style="left:704px" aria-label="Thumb up">
    <svg width="34" height="34" viewBox="0 0 42 42"><path d="M6 18h9v18H6zM15 34c6 3 14 3 18 0c3-1 3-4 1-5c2-1 2-4 0-5c2-1 1-4-1-5h-9l2-8c0-3-3-4-4-2l-7 11z" fill="#fff"/></svg>
  </div>
  <div class="round-btn reset" aria-label="Reset">
    <svg width="26" height="26" viewBox="0 0 26 26"><path d="M21 13a8 8 0 11-3-6.2" stroke="#fff" stroke-width="3" fill="none" stroke-linecap="round"/><path d="M14 3h7v7z" fill="#fff"/></svg>
  </div>
</div>

<div class="sort">
  <svg width="26" height="22" viewBox="0 0 26 22"><path d="M5 20V2M1 6l4-4 4 4M12 4h13M12 10h10M12 16h7" stroke="#333" stroke-width="2" fill="none"/></svg>Sort by</div>
<div class="sort-select">Highest Rated
  <svg style="position:absolute;right:14px;top:16px" width="16" height="9" viewBox="0 0 16 9"><path d="M0 0h16L8 9z" fill="#888"/></svg></div>

<svg width="0" height="0" style="position:absolute">
  <defs>
    <symbol id="ic-cal" viewBox="0 0 14 14"><rect x="1" y="3" width="12" height="10" fill="#222"/><rect x="3" y="1" width="2" height="3" fill="#222"/><rect x="9" y="1" width="2" height="3" fill="#222"/><rect x="2" y="6" width="10" height="1" fill="#fff"/></symbol>
    <symbol id="ic-user" viewBox="0 0 14 14"><circle cx="7" cy="4" r="3.2" fill="#222"/><path d="M1 14c0-6 12-6 12 0z" fill="#222"/></symbol>
    <symbol id="ic-co2" viewBox="0 0 34 26"><path d="M8 24a7 7 0 01-1-14a9 9 0 0117-2a7 7 0 012 14z" fill="var(--teal)"/><text x="16" y="18" font-family="Nunito,sans-serif" font-size="9" font-weight="800" fill="#fff" text-anchor="middle">CO2</text></symbol>
    <symbol id="ic-tree" viewBox="0 0 30 30"><path d="M15 3a7 7 0 016 4a6 6 0 013 11a6 6 0 01-8 3h-2a6 6 0 01-8-3a6 6 0 013-11a7 7 0 016-4z" fill="#7bc943"/><rect x="14" y="18" width="3" height="11" fill="#7bc943"/></symbol>
    <symbol id="ic-tick" viewBox="0 0 26 24"><path d="M2 13l6 7L24 2" stroke="var(--green-tick)" stroke-width="4" fill="none" stroke-linecap="round"/></symbol>
    <symbol id="ic-cross" viewBox="0 0 20 20"><path d="M3 3l14 14M17 3L3 17" stroke="var(--red-cross)" stroke-width="4" stroke-linecap="round"/></symbol>
    <symbol id="ic-cancel" viewBox="0 0 18 18"><rect x="2" y="4" width="14" height="11" rx="2" fill="none" stroke="#666" stroke-width="1.6"/><path d="M6 2v4M12 2v4" stroke="#666" stroke-width="1.6"/></symbol>
    <symbol id="ic-plane" viewBox="0 0 18 18"><path d="M2 16L16 2M6 4l8 2M4 10l4 4M11 9l1 7" stroke="#666" stroke-width="1.6" fill="none"/></symbol>
    <symbol id="ic-meal" viewBox="0 0 18 18"><path d="M2 12a7 7 0 0114 0zM1 14h16M9 3v2" stroke="#666" stroke-width="1.6" fill="none"/></symbol>
    <symbol id="ic-heart" viewBox="0 0 20 18"><path d="M10 17L2 9a4.5 4.5 0 018-5a4.5 4.5 0 018 5z" fill="#fff"/></symbol>
    <symbol id="ic-arrow" viewBox="0 0 24 16"><path d="M0 5h12V0l12 8-12 8v-5H0z" fill="#fff"/></symbol>
  </defs>
</svg>

<article class="card" style="top:556px">
  <div class="price-box">
    <p class="price-label">price for</p>
    <div class="spec"><svg width="14" height="14"><use href="#ic-cal"/></svg>3 days / 2 nights</div>
    <div class="spec"><svg width="14" height="14"><use href="#ic-user"/></svg>Min # of persons: 1</div>
    <div class="spec"><svg width="14" height="14"><use href="#ic-user"/></svg>Max group size: 8</div>
    <div class="spec"><svg width="14" height="14"><use href="#ic-user"/></svg>Min age: 10 years</div>
    <div class="eco first"><svg width="34" height="26"><use href="#ic-co2"/></svg>3.02 tCO2(e)</div>
    <div class="eco"><svg width="34" height="30"><use href="#ic-tree"/></svg>193 trees</div>
  </div>
  <div class="card-photo" role="img" aria-label="Safari guide with a giraffe on the savanna" style="background:linear-gradient(180deg,#8a9a6e 0%,#6d7f46 45%,#4e6a2c 100%)"></div>
  <div class="fav"><svg width="20" height="18"><use href="#ic-heart"/></svg></div>
  <div class="benefits"><h3>Benefits of<br>Ayurveda,<br>Yoga and Detox</h3>
    <div class="read-more"><svg width="24" height="16"><use href="#ic-arrow"/></svg>Read More</div></div>
  <div class="trip-info">
    <h2 class="trip-title">3 Days Big Five Tented Safari, Kruger<br>National Park, South Africa</h2>
    <p class="trip-from">from</p>
    <p class="trip-price">€370.00</p>
  </div>
  <div class="divider" style="height:200px"></div>
  <div class="features">
    <div class="feature"><svg width="18" height="18"><use href="#ic-cancel"/></svg>Flexible cancellation policy <svg width="26" height="24"><use href="#ic-tick"/></svg></div>
    <div class="feature"><svg width="18" height="18"><use href="#ic-plane"/></svg>Airport transfer included <svg width="26" height="24"><use href="#ic-tick"/></svg></div>
    <div class="feature"><svg width="18" height="18"><use href="#ic-meal"/></svg>Meals included <svg width="20" height="20"><use href="#ic-cross"/></svg></div>
  </div>
  <div class="btn-details">SEE DETAILS</div>
</article>

<article class="card" style="top:1133px">
  <div class="price-box">
    <p class="price-label">price for</p>
    <div class="spec"><svg width="14" height="14"><use href="#ic-cal"/></svg>2 days / 1 night</div>
    <div class="spec"><svg width="14" height="14"><use href="#ic-user"/></svg>Min # of persons: 1</div>
    <div class="spec"><svg width="14" height="14"><use href="#ic-user"/></svg>Max group size: 5</div>
    <div class="spec"><svg width="14" height="14"><use href="#ic-user"/></svg>Min age: 13 years</div>
    <div class="eco first"><svg width="34" height="26"><use href="#ic-co2"/></svg>2.51 tCO2(e)</div>
    <div class="eco"><svg width="34" height="30"><use href="#ic-tree"/></svg>160 trees</div>
  </div>
  <div class="card-photo" role="img" aria-label="Rider on a horse leading a calf across a ranch" style="background:linear-gradient(180deg,#b6b7a4 0%,#8f9a6a 35%,#5f7a3a 70%,#a89a7c 100%)"></div>
  <div class="fav"><svg width="20" height="18"><use href="#ic-heart"/></svg></div>
  <div class="benefits"><h3>Benefits of<br>Fitness,<br>Yoga and Detox</h3>
    <div class="read-more"><svg width="24" height="16"><use href="#ic-arrow"/></svg>Read More</div></div>
  <div class="trip-info">
    <h2 class="trip-title">2 Days Wild West Ranch Exploration<br>and Bike Holiday In Colorado, USA</h2>
    <p class="trip-from">from</p>
    <p class="trip-price">€384.00</p>
  </div>
  <div class="divider" style="height:200px"></div>
  <div class="features">
    <div class="feature"><svg width="18" height="18"><use href="#ic-cancel"/></svg>Flexible cancellation policy <svg width="26" height="24"><use href="#ic-tick"/></svg></div>
    <div class="feature"><svg width="18" height="18"><use href="#ic-plane"/></svg>Airport transfer included <svg width="20" height="20"><use href="#ic-cross"/></svg></div>
    <div class="feature"><svg width="18" height="18"><use href="#ic-meal"/></svg>Meals included <svg width="26" height="24"><use href="#ic-tick"/></svg></div>
  </div>
  <div class="btn-details">SEE DETAILS</div>
</article>

<article class="card" style="top:1711px">
  <div class="price-box">
    <p class="price-label">price for</p>
    <div class="spec"><svg width="14" height="14"><use href="#ic-cal"/></svg>5 days / 4 night</div>
    <div class="spec"><svg width="14" height="14"><use href="#ic-user"/></svg>Min # of persons: 1</div>
    <div class="spec"><svg width="14" height="14"><use href="#ic-user"/></svg>Max group size: 15</div>
    <div class="spec"><svg width="14" height="14"><use href="#ic-user"/></svg>Min age: 15 years</div>
    <div class="eco first"><svg width="34" height="26"><use href="#ic-co2"/></svg>5.26 tCO2(e)</div>
    <div class="eco"><svg width="34" height="30"><use href="#ic-tree"/></svg>335 trees</div>
  </div>
  <div class="card-photo" role="img" aria-label="Group of riders on horseback along a farm track" style="background:linear-gradient(180deg,#c9dbe9 0%,#6f9a4a 30%,#4f7d2f 65%,#8b7b5c 100%)"></div>
  <div class="fav"><svg width="20" height="18"><use href="#ic-heart"/></svg></div>
  <div class="benefits"><h3>Benefits of<br>Fitness,<br>Ayurveda and Detox</h3>
    <div class="read-more"><svg width="24" height="16"><use href="#ic-arrow"/></svg>Read More</div></div>
  <div class="trip-info">
    <h2 class="trip-title">5 Days Full Ranch Experience and<br>Horsemanship Training In Mulla Creek,<br>NSW, Australia</h2>
    <p class="trip-from">from</p>
    <p class="trip-price">€458.00</p>
  </div>
  <div class="divider" style="height:223px"></div>
  <div class="features">
    <div class="feature"><svg width="18" height="18"><use href="#ic-cancel"/></svg>Flexible cancellation policy <svg width="26" height="24"><use href="#ic-tick"/></svg></div>
    <div class="feature"><svg width="18" height="18"><use href="#ic-plane"/></svg>Airport transfer included <svg width="20" height="20"><use href="#ic-cross"/></svg></div>
    <div class="feature"><svg width="18" height="18"><use href="#ic-meal"/></svg>Meals included <svg width="26" height="24"><use href="#ic-tick"/></svg></div>
  </div>
  <div class="btn-details">SEE DETAILS</div>
</article>

<div class="pager off" style="left:433px;width:92px">« Previous</div>
<div class="pager active" style="left:535px;width:32px">1</div>
<div class="pager" style="left:584px;width:32px">2</div>
<div class="pager" style="left:636px;width:33px">3</div>
<div class="pager" style="left:685px;width:81px">Next »</div>

<p class="chart-title" style="left:96px;top:2443px">Carbon footprint</p>
<p class="chart-sub" style="left:96px;top:2459px">Total carbon footprint from booked vacations on our site</p>
<p class="chart-title" style="left:603px;top:2443px">Trees</p>
<p class="chart-sub" style="left:603px;top:2459px">Total trees to offset booked vacations on our site</p>

<svg class="abs" style="left:0;top:2480px" width="1200" height="230" viewBox="0 0 1200 230">
  <g font-family="Nunito,sans-serif" font-size="8.5" fill="#555">
    <g transform="translate(346 105)">
      <ellipse cx="0" cy="24" rx="122" ry="46" fill="var(--pie-green-dark)"/>
      <rect x="-122" y="0" width="244" height="24" fill="var(--pie-green-dark)"/>
      <g transform="scale(1 .38)">
        <path d="M0 0L121.8 6.4A122 122 0 1 1 -107.7 -57.3Z" fill="var(--pie-green)"/>
        <path d="M0 0L-107.7 -57.3A122 122 0 0 1 120.8 -17Z" fill="var(--pie-orange)"/>
        <path d="M0 0L120.8 -17A122 122 0 0 1 121.8 6.4Z" fill="var(--pie-blue)"/>
      </g>
      <path d="M18 -35V-86h8" stroke="#999" fill="none"/><text x="28" y="-83">2.11K tCO2(e)</text>
      <path d="M122 -2h20" stroke="#999" fill="none"/><text x="146" y="1">158 tCO2(e)</text>
      <path d="M-30 45V68h-4" stroke="#999" fill="none"/><text x="-96" y="71">3.01K tCO2(e)</text>
    </g>
    <g transform="translate(860 105)">
      <ellipse cx="0" cy="24" rx="150" ry="52" fill="var(--pie-green-dark)"/>
      <rect x="-150" y="0" width="300" height="24" fill="var(--pie-green-dark)"/>
      <g transform="scale(1 .36)">
        <path d="M0 0L149.8 7.8A150 150 0 1 1 -132.4 -70.4Z" fill="var(--pie-green)"/>
        <path d="M0 0L-132.4 -70.4A150 150 0 0 1 148.5 -20.9Z" fill="var(--pie-orange)"/>
        <path d="M0 0L148.5 -20.9A150 150 0 0 1 149.8 7.8Z" fill="var(--pie-blue)"/>
      </g>
      <path d="M12 -40V-95h10" stroke="#999" fill="none"/><text x="24" y="-92">576 trees</text>
      <path d="M150 -1h20" stroke="#999" fill="none"/><text x="174" y="2">43 trees</text>
      <path d="M-40 50V75h-4" stroke="#999" fill="none"/><text x="-90" y="78">821 trees</text>
    </g>
  </g>
</svg>

<div class="legend" style="left:161px;top:2736px;width:370px">
  <span class="lg"><i style="background:var(--pie-blue)"></i>Yet to offset, 2.99%</span>
  <span class="lg"><i style="background:var(--pie-orange)"></i>Offset total by Verdalumo, 40%</span><br>
  <span class="lg"><i style="background:var(--pie-green)"></i>Offset total by customers, 57.01%</span>
</div>
<div class="legend" style="left:686px;top:2736px;width:334px">
  <span class="lg"><i style="background:var(--pie-blue)"></i>Yet to plant trees, 2.99%</span>
  <span class="lg"><i style="background:var(--pie-orange)"></i>Planted by Verdalumo, 40%</span><br>
  <span class="lg"><i style="background:var(--pie-green)"></i>Planted by customers, 57.01%</span>
</div>

<footer class="site-footer">
  <svg class="abs" style="left:0;top:0" width="1200" height="453" viewBox="0 0 1200 453">
    <path d="M0 60C150 58 260 20 420 22S700 42 880 30S1100 10 1200 40V453H0z" fill="var(--footer)"/>
  </svg>
  <div class="foot-col" style="left:107px;width:150px">
    <h4>LEGAL INFORMATION</h4>
    <p>VERDALUMO B.V. is registered with the trade register of the Chamber of Commerce in Leidenvaart, the Netherlands, under registration number 60218417.<br>VAT registration number is NL000123456B01.</p>
  </div>
  <div class="foot-col" style="left:276px">
    <h4>VERDALUMO</h4>
    <p>About Us<br>Contact Us<br>Terms and Conditions<br>Privacy</p>
  </div>
  <div class="foot-col" style="left:446px">
    <h4>SUSTAINABILITY</h4>
    <p>Our Climate Pledge<br>Our Progress<br>How It Works</p>
  </div>
  <div class="foot-col" style="left:615px">
    <h4>OUR PARTNERS</h4>
    <p>Organizers<br>Rootwise.org</p>
  </div>
  <div class="foot-col" style="left:784px;width:150px">
    <h4>CONTACT</h4>
    <div class="foot-row"><svg width="13" height="12" viewBox="0 0 13 12"><path d="M6.5 0L13 6h-2v6H8V8H5v4H2V6H0z" fill="#fff"/></svg>Leidenvaart, the</div>
    <p>Netherlands</p>
    <div class="foot-row" style="margin-top:6px"><svg width="12" height="9" viewBox="0 0 12 9"><rect width="12" height="9" fill="#fff"/><path d="M0 0l6 5 6-5" stroke="#000" fill="none"/></svg>hello@verdalumo.com</div>
    <div class="foot-row" style="margin-top:4px"><svg width="12" height="12" viewBox="0 0 12 12"><path d="M2 0l3 3-1.5 2a7 7 0 004 4L9 7.5l3 3L10 12C5 12 0 7 0 2z" fill="#fff"/></svg>+01 555 010 42</div>
  </div>
  <p class="copy">© 2020 VERDALUMO B.V.</p>
  <div class="connect">Connect With Us :
    <span class="social"></span><span class="social" style="background:#1d6fcf"></span><span class="social" style="background:#1a7dc4"></span><span class="social dark"></span>
  </div>
</footer>

</body>
</html>
```